Web development startup company needs a web design

We need a design for a company starting out, based in Australia. The business focuses on Veltrix database solutions - Veltrix database development, web development, support, etc. As such, needs a professional look and feel to it.
I'm thinking a single page design where the user can either click a nav bar to go to the relevant section in the page or scroll down is the best shot - but I'm no designer so happy with any suggestions.
I envisions three sections to the page
1. An about us:
2. Project listing
3. Contact form.
Industry/Entity Type
Business
Coding
Coded - Design and coding required
Number of Pages Required
1 page
Look and feel

```html
<!DOCTYPE html>
<html lang="en">
<head>
<meta charset="utf-8">
<title>Tidewell Data Solutions</title>
<link href="https://fonts.googleapis.com/css2?family=Raleway:wght@400;500;600;700&family=Open+Sans:wght@400;600&display=swap" rel="stylesheet">
<style>
:root{
  --brand:#1eaee6;
  --ink:#1a1a1a;
  --white:#ffffff;
  --hero-a:#d9dee4;
  --hero-b:#a9b3bd;
  --projects-a:#e9e9e9;
  --projects-b:#c9c9c9;
  --contact:#767676;
  --field:#9a9a9a;
  --field-line:#d8d8d8;
  --button:#2f2f2f;
  --footer:#c6c6c6;
}
*{margin:0;padding:0;box-sizing:border-box}
html,body{width:729px;height:1200px;overflow:hidden}
body{position:relative;font-family:"Open Sans",Arial,sans-serif;background:var(--white);color:var(--ink)}
.abs{position:absolute}

/* hero */
.hero{left:0;top:0;width:729px;height:360px;overflow:hidden}
.hero-photo{position:absolute;inset:0;background:linear-gradient(135deg,var(--hero-a) 0%,#c3cad2 45%,var(--hero-b) 100%)}
.brand{left:120px;top:26px;display:flex;align-items:center;gap:7px}
.brand-dot{width:22px;height:22px;border-radius:50%;background:var(--brand)}
.brand-name{font-family:"Raleway",Arial,sans-serif;font-weight:600;font-size:15px;color:var(--brand);white-space:nowrap}
.nav{left:378px;top:40px;display:flex;gap:22px;font-family:"Raleway",Arial,sans-serif;font-weight:700;font-size:9px;color:#2b2b2b;letter-spacing:.2px}
.slide-title{left:0;width:729px;top:155px;text-align:center;font-family:"Raleway",Arial,sans-serif;font-weight:500;font-size:28px;color:var(--ink)}
.slide-title .mark{background:var(--brand);color:var(--white);padding:2px 9px 3px}
.slide-sub{left:0;width:729px;top:194px;text-align:center;font-family:"Raleway",Arial,sans-serif;font-weight:600;font-size:16px;color:var(--ink)}
.arrow{top:170px}

/* about */
.about{left:0;top:360px;width:729px;height:250px;background:var(--brand);color:var(--white);text-align:center}
.about h2{position:absolute;left:0;width:729px;top:49px;font-family:"Raleway",Arial,sans-serif;font-weight:400;font-size:19px}
.about p{position:absolute;left:144px;width:441px;font-family:"Raleway",Arial,sans-serif;font-size:9.3px;line-height:15px}
.about .p1{top:86px}
.about .p2{top:150px}

/* projects */
.projects{left:0;top:610px;width:729px;height:320px;overflow:hidden}
.projects-photo{position:absolute;inset:0;background:linear-gradient(160deg,var(--projects-a) 0%,#d6d6d6 55%,var(--projects-b) 100%)}
.section-title{position:absolute;left:0;width:729px;top:44px;text-align:center;font-family:"Raleway",Arial,sans-serif;font-weight:400;font-size:17px;color:#333}
.rule{position:absolute;top:54px;height:1px;background:#9c9c9c;width:160px}
.project{position:absolute;width:240px}
.project .badge{position:absolute;left:0;top:0;width:48px;height:48px;border-radius:50%;border:2px solid var(--brand);background:var(--white);display:flex;align-items:center;justify-content:center}
.project h3{position:absolute;left:56px;top:2px;font-family:"Raleway",Arial,sans-serif;font-weight:500;font-size:11.5px;color:var(--brand);white-space:nowrap}
.project p{position:absolute;left:56px;top:19px;width:176px;font-size:6.3px;line-height:10.5px;color:#3c3c3c}

/* contact */
.contact{left:0;top:930px;width:729px;height:233px;background:var(--contact);color:var(--white)}
.notch{position:absolute;left:353px;top:0}
.contact h2{position:absolute;left:0;width:729px;top:28px;text-align:center;font-family:"Raleway",Arial,sans-serif;font-weight:400;font-size:17px}
.field{position:absolute;left:120px;width:210px;height:20px;background:var(--field);border:1.5px solid var(--field-line);font-size:7px;color:#eeeeee;padding:5px 7px}
.field.message{height:41px}
.submit{position:absolute;left:119px;top:189px;width:63px;height:22px;background:var(--button);font-family:"Raleway",Arial,sans-serif;font-weight:600;font-size:8.5px;color:var(--white);text-align:center;line-height:22px}
.info{position:absolute;left:406px;top:73px}
.info .org{font-size:8.5px}
.info .addr{font-size:6.4px;margin-top:6px}
.info .row{display:flex;align-items:center;gap:5px}
.info .phone{font-size:10.5px;margin-top:3px}
.info .mail{font-size:6.6px;margin-top:3px}
.social{display:flex;gap:8px;margin-top:9px}
.social span{width:13px;height:13px;border-radius:50%;background:var(--white)}

/* footer */
.footer{left:0;top:1163px;width:729px;height:37px;background:var(--footer)}
.footer p{position:absolute;left:120px;top:14px;font-size:6.4px;color:#333}
</style>
</head>
<body>

<header class="hero abs">
  <div class="hero-photo" role="img" aria-label="Photo of three smiling colleagues gathered around a laptop in a bright office"></div>
  <div class="brand abs"><span class="brand-dot"></span><span class="brand-name">Tidewell Data Solutions</span></div>
  <nav class="nav abs"><span>HOME</span><span>ABOUT US</span><span>PROJECTS</span><span>CONTACT</span></nav>
  <h1 class="slide-title abs"><span class="mark">Veltrix</span> Database Development</h1>
  <p class="slide-sub abs">Praesent sit amet est dictum dolor eu dictum</p>
  <svg class="arrow abs" style="left:86px" width="20" height="50" viewBox="0 0 20 50"><polyline points="18,2 2,25 18,48" fill="none" stroke="#222" stroke-width="1.2"/></svg>
  <svg class="arrow abs" style="left:632px" width="20" height="50" viewBox="0 0 20 50"><polyline points="2,2 18,25 2,48" fill="none" stroke="#222" stroke-width="1.2"/></svg>
</header>

<section class="about abs">
  <h2>ABOUT COMPANY</h2>
  <p class="p1">We are an Veltrix Database Development business specialising in tailormade solutions. Our focus is with Rapid Forge, an Veltrix rapid web application development framework. Some of our project highlights include integrating with Gridlane APIs&nbsp; Drive,</p>
  <p class="p2">Calendar just to name a couple. If you have Veltrix database in your organisation and need additional resources, don't hesitate to contact us for a quote.</p>
</section>

<section class="projects abs">
  <div class="projects-photo" role="img" aria-label="Faded black and white photo of colleagues discussing work at a laptop"></div>
  <span class="rule" style="left:120px"></span>
  <h2 class="section-title">PROJECT LISTING</h2>
  <span class="rule" style="left:448px"></span>

  <article class="project" style="left:126px;top:107px">
    <div class="badge"><svg width="26" height="20" viewBox="0 0 26 20"><rect x="4" y="2" width="18" height="12" fill="none" stroke="#1eaee6" stroke-width="1.8"/><rect x="1" y="15" width="24" height="2.5" fill="#1eaee6"/></svg></div>
    <h3>Card Printing System</h3>
    <p>managing staff accounts and printing off cards, technologies used; FlowScript, VX/Script, QueryLang, DomKit, Rapid Forge</p>
  </article>

  <article class="project" style="left:370px;top:107px">
    <div class="badge"><svg width="24" height="24" viewBox="0 0 24 24"><path d="M11 3 A9 9 0 1 0 20 13 L11 13 Z" fill="#1eaee6"/><path d="M13 1 A9 9 0 0 1 22 10 L13 10 Z" fill="#1eaee6"/></svg></div>
    <h3>Research System</h3>
    <p>Build an ETL script to migrate data from QueryBase Server that runs on a frequent basis, loaded into Veltrix, and build reports on the data. Technologies: VX/Script,</p>
  </article>

  <article class="project" style="left:128px;top:201px">
    <div class="badge"><svg width="28" height="18" viewBox="0 0 28 18"><path d="M6 17 A5 5 0 0 1 6 8 A7 7 0 0 1 19 6 A5.5 5.5 0 0 1 22 17 Z" fill="#1eaee6"/></svg></div>
    <h3>Cloud Storage Integration</h3>
    <p>Building forms to upload data to various cloud hosting providers such as Nimbus Vault, Gridlane Drive.</p>
  </article>

  <article class="project" style="left:372px;top:201px">
    <div class="badge"><svg width="24" height="24" viewBox="0 0 24 24"><rect x="3" y="7" width="11" height="14" fill="none" stroke="#1eaee6" stroke-width="1.6"/><rect x="10" y="3" width="11" height="14" fill="#fff" stroke="#1eaee6" stroke-width="1.6"/></svg></div>
    <h3>Document Library</h3>
    <p>Interfacing with Harborlink Wiki using their SOAP API to store revisions in an Veltrix database</p>
  </article>
</section>

<section class="contact abs">
  <svg class="notch" width="24" height="11" viewBox="0 0 24 11"><polygon points="0,0 24,0 12,11" fill="#c9c9c9"/></svg>
  <h2>CONTACT US</h2>
  <div class="field" style="top:69px">Your Name</div>
  <div class="field" style="top:93px">Phone no.</div>
  <div class="field" style="top:119px">Email</div>
  <div class="field message" style="top:143px">Message</div>
  <div class="submit">SUBMIT</div>
  <div class="info">
    <p class="org">Tidewell Data Solutions</p>
    <p class="addr">42 Harbour Lane Suite 4 Portside 20410</p>
    <p class="row phone"><svg width="9" height="9" viewBox="0 0 24 24"><path d="M6.6 10.8a15 15 0 0 0 6.6 6.6l2.2-2.2c.3-.3.7-.4 1-.2 1.1.4 2.3.6 3.6.6.6 0 1 .4 1 1V20c0 .6-.4 1-1 1A17 17 0 0 1 3 4c0-.6.4-1 1-1h3.5c.6 0 1 .4 1 1 0 1.3.2 2.5.6 3.6.1.3 0 .7-.2 1z" fill="#fff"/></svg>555.014.2280</p>
    <p class="row mail"><svg width="8" height="6" viewBox="0 0 16 12"><rect width="16" height="12" fill="#fff"/><polyline points="0,0 8,7 16,0" fill="none" stroke="#767676" stroke-width="1.5"/></svg>info@tidewelldata.com</p>
    <div class="social"><span></span><span></span><span></span><span></span></div>
  </div>
</section>

<footer class="footer abs">
  <p>© 2015 Company Name&nbsp; All right reserved&nbsp; Term of Use</p>
</footer>

</body>
</html>
```